Business Card Design Project

I have just chosen a logo and would now like this designed onto a business card for my hair salon. I would like it to be classy not to busy and have a wow factor when people look at them
Has to Include on card:
Logo Design
And business details below
Kellie-ann Drummond (owner)
0482 736 219
Rdw@vomblet.com.au
71 Willowmere Rise Corvin Cove
Logo is now attached please provide designs
Hair

```html
<!DOCTYPE html>
<html lang="en">
<head>
<meta charset="utf-8">
<title>Velvet Row Hair Studio – Business Card</title>
<link rel="stylesheet" href="https://fonts.googleapis.com/css2?family=Source+Sans+3:wght@400;600&family=Roboto+Condensed:wght@400&display=swap">
<style>
  :root {
    --canvas-bg: #f4f4f4;
    --card-base: #242426;
    --card-tile-light: #333336;
    --card-tile-dark: #1b1b1d;
    --accent-pink: #e0187a;
    --accent-teal: #2fb5c8;
    --text-light: #f2f2f2;
    --divider: #e6e6e6;
  }
  * { box-sizing: border-box; margin: 0; padding: 0; }
  html, body {
    width: 1200px;
    height: 800px;
    overflow: hidden;
    background: var(--canvas-bg);
  }
  .canvas {
    position: relative;
    width: 1200px;
    height: 800px;
  }
  .business-card {
    position: absolute;
    left: 150px;
    top: 143px;
    width: 900px;
    height: 514px;
    background: var(--card-base);
    overflow: hidden;
    box-shadow: 0 6px 18px rgba(0, 0, 0, 0.18);
  }
  .card-texture {
    position: absolute;
    inset: 0;
    background:
      radial-gradient(ellipse at 70% 85%, rgba(120, 120, 125, 0.35), transparent 55%),
      radial-gradient(ellipse at 20% 20%, rgba(90, 90, 95, 0.25), transparent 50%),
      linear-gradient(160deg, var(--card-tile-light), var(--card-tile-dark));
  }
  .owner-name {
    position: absolute;
    right: 58px;
    top: 40px;
    font-family: "Source Sans 3", sans-serif;
    font-weight: 400;
    font-size: 30px;
    color: var(--accent-pink);
    letter-spacing: 0.3px;
  }
  .brand {
    position: absolute;
    left: 60px;
    top: 170px;
    width: 340px;
    display: flex;
    align-items: center;
    gap: 18px;
  }
  .brand-mark {
    flex: none;
    width: 44px;
    height: 44px;
    border-radius: 50%;
    background: var(--accent-teal);
  }
  .brand-name {
    font-family: "Source Sans 3", sans-serif;
    font-weight: 600;
    font-size: 46px;
    line-height: 1.05;
    color: var(--accent-pink);
    text-transform: uppercase;
    letter-spacing: 1px;
  }
  .divider {
    position: absolute;
    left: 430px;
    top: 140px;
    width: 2px;
    height: 270px;
    background: var(--divider);
  }
  .contact-details {
    position: absolute;
    left: 470px;
    top: 200px;
    list-style: none;
    font-family: "Roboto Condensed", sans-serif;
    font-size: 26px;
    line-height: 1.4;
    color: var(--text-light);
  }
</style>
</head>
<body>
  <main class="canvas">
    <section class="business-card">
      <div class="card-texture" role="img" aria-label="Dark charcoal mosaic tile texture with scattered lighter squares"></div>

      <p class="owner-name">Kellie-ann Drummond</p>

      <div class="brand">
        <span class="brand-mark" aria-hidden="true"></span>
        <p class="brand-name">Velvet Row Hair Studio</p>
      </div>

      <div class="divider" aria-hidden="true"></div>

      <ul class="contact-details">
        <li class="contact-address">71 Willowmere Rise Corvin Cove</li>
        <li class="contact-email">Rdw@vomblet.com.au</li>
        <li class="contact-phone">0482 736 219</li>
      </ul>
    </section>
  </main>
</body>
</html>
```